Greta's Hair and Wigs: Back to School Sale

I need a "Back to School" sale flyer: I sell hair extensions and fashion wigs to a very diverse clientele. The sale will include:
20% OFF: Synthetic Hair Extensions
20% OFF: Synthetic Hair Pieces
15% OFF: Human Hair Extensions
25% OFF: Jewelry/Accessories
Starts: Thursday, August 3rd to Saturday, August 5th

Target Market(s)

women of all ethnic backgrounds and between the ages of 16-60

Industry/Entity Type

Hair And Beauty

Font styles to use
Sans Serif

Colors
e34197

Requirements
Must have
• High resolution for printing posters and flyers. As well as posting on social media: Instagram/Facebook
• Eye catching graphics

```html
<!DOCTYPE html>
<html lang="en">
<head>
<meta charset="utf-8">
<title>Greta's Hair and Wigs – Back to School Offers</title>
<link rel="stylesheet" href="https://fonts.googleapis.com/css2?family=Cinzel:wght@400&family=Playfair+Display:wght@400;700;900&display=swap">
<style>
  :root {
    --magenta: #c92c87;
    --circle-outer: #cd3d90;
    --circle-mid: #d04895;
    --circle-inner: #d35aa2;
    --white: #ffffff;
    --ink: #1c1c1c;
    --grey-text: #3a3a3a;
    --rule: #cfcfcf;
    --mint: #5ec49f;
    --mint-dark: #3f9b80;
    --mint-fold: #2f7a63;
    --tag-red: #e02230;
    --serif: 'Playfair Display', Georgia, serif;
    --caps: 'Cinzel', 'Times New Roman', serif;
  }
  * { margin: 0; padding: 0; box-sizing: border-box; }
  html, body { width: 880px; height: 1200px; overflow: hidden; background: var(--magenta); }
  .flyer {
    position: relative;
    width: 880px;
    height: 1200px;
    background-color: var(--magenta);
    background-image:
      linear-gradient(rgba(255,255,255,0.045) 1px, transparent 1px),
      linear-gradient(90deg, rgba(255,255,255,0.045) 1px, transparent 1px);
    background-size: 22px 22px;
    overflow: hidden;
  }
  .frame {
    position: absolute;
    left: 28px; top: 30px; right: 28px; bottom: 28px;
    border: 2px solid var(--white);
  }
  .headline-art { position: absolute; left: 0; top: 0; width: 880px; height: 1200px; }

  .brand-tag {
    position: absolute;
    left: 63px; top: 30px;
    width: 131px; height: 188px;
  }
  .brand-tag svg { position: absolute; inset: 0; }
  .brand-tag__body {
    position: relative;
    display: flex;
    flex-direction: column;
    align-items: center;
    padding-top: 26px;
  }
  .brand-tag__mark {
    width: 34px; height: 34px;
    background: var(--magenta);
    margin-bottom: 14px;
  }
  .brand-tag__name {
    font-family: var(--serif);
    font-weight: 400;
    font-size: 17px;
    line-height: 21px;
    color: var(--grey-text);
    text-align: center;
  }

  .coupon {
    position: absolute;
    width: 290px; height: 173px;
  }
  .coupon svg { position: absolute; inset: 0; }
  .coupon__figure {
    position: absolute;
    left: 0; right: 0; top: 28px;
    display: flex;
    justify-content: center;
    align-items: flex-start;
    color: var(--ink);
  }
  .coupon__number {
    font-family: var(--caps);
    font-weight: 400;
    font-size: 92px;
    line-height: 78px;
    letter-spacing: -2px;
  }
  .coupon__unit {
    font-family: var(--caps);
    font-size: 26px;
    line-height: 1;
    margin-left: 12px;
    margin-top: 6px;
  }
  .coupon__unit span { display: block; }
  .coupon__pct { font-family: var(--serif); font-size: 22px; }
  .coupon__rule {
    position: absolute;
    left: 27px; right: 27px; top: 119px;
    height: 1px; background: var(--rule);
  }
  .coupon__label {
    position: absolute;
    left: 0; right: 0; top: 130px;
    text-align: center;
    font-family: var(--serif);
    font-size: 17px;
    color: var(--ink);
  }
</style>
</head>
<body>
<main class="flyer">
  <div class="frame"></div>

  <svg class="headline-art" viewBox="0 0 880 1200" xmlns="http://www.w3.org/2000/svg">
    <circle cx="451" cy="432" r="388" fill="var(--circle-outer)"/>
    <circle cx="451" cy="432" r="362" fill="var(--circle-mid)"/>
    <circle cx="451" cy="432" r="332" fill="var(--circle-inner)"/>

    <g class="headline" transform="translate(441,340) rotate(-15)" fill="var(--white)" font-family="Playfair Display, Georgia, serif" font-weight="900">
      <text x="20" y="-54" font-size="124" text-anchor="middle" textLength="390" lengthAdjust="spacingAndGlyphs">BACK</text>
      <polygon points="-272,6 -72,-1 -72,7"/>
      <text x="-8" y="24" font-size="66" text-anchor="middle" textLength="104" lengthAdjust="spacingAndGlyphs">TO</text>
      <polygon points="56,-3 272,-12 56,5"/>
      <text x="-38" y="150" font-size="146" text-anchor="middle" textLength="705" lengthAdjust="spacingAndGlyphs">SCHOOL</text>
    </g>

    <g class="offers-tag">
      <path d="M716,332 C694,322 700,290 724,284" fill="none" stroke="#333" stroke-width="1.5"/>
      <g transform="translate(770,292) rotate(-22)">
        <path d="M-44,0 L-30,-15 H46 V15 H-30 Z" fill="var(--tag-red)"/>
        <circle cx="-33" cy="0" r="2.5" fill="#f4a0a8"/>
        <text x="10" y="6" font-family="Playfair Display, Georgia, serif" font-weight="700" font-size="18" fill="var(--white)" text-anchor="middle">Offers</text>
      </g>
    </g>

    <g class="date-ribbon" transform="translate(440,573) rotate(-16)">
      <polygon points="-330,-12 -400,-12 -380,12 -400,38 -330,38" fill="var(--mint-dark)"/>
      <polygon points="-350,25 -330,38 -330,25" fill="var(--mint-fold)"/>
      <polygon points="330,-38 400,-38 380,-12 400,12 330,12" fill="var(--mint-dark)"/>
      <polygon points="350,-25 330,-38 330,-25" fill="var(--mint-fold)"/>
      <rect x="-350" y="-25" width="700" height="50" fill="var(--mint)"/>
      <text x="0" y="9" font-family="Playfair Display, Georgia, serif" font-size="27" fill="var(--white)" text-anchor="middle" textLength="625" lengthAdjust="spacingAndGlyphs">Starts: 3rd-5th, August | Thursday - Saturday</text>
    </g>
  </svg>

  <div class="brand-tag">
    <svg viewBox="0 0 131 188" width="131" height="188">
      <polygon points="0,0 131,0 131,188 65.5,168 0,188" fill="var(--white)"/>
    </svg>
    <div class="brand-tag__body">
      <div class="brand-tag__mark"></div>
      <div class="brand-tag__name">Greta's<br>Hair and<br>Wigs</div>
    </div>
  </div>

  <article class="coupon" style="left:123px; top:712px;">
    <svg viewBox="0 0 290 173" width="290" height="173">
      <path d="M16,0 H274 A16,16 0 0 0 290,16 V157 A16,16 0 0 0 274,173 H16 A16,16 0 0 0 0,157 V16 A16,16 0 0 0 16,0 Z" fill="var(--white)"/>
      <path d="M22,6 H268 A16,16 0 0 0 284,22 V151 A16,16 0 0 0 268,167 H22 A16,16 0 0 0 6,151 V22 A16,16 0 0 0 22,6 Z" fill="none" stroke="var(--magenta)" stroke-width="1.2"/>
    </svg>
    <div class="coupon__figure"><span class="coupon__number">20</span><span class="coupon__unit"><span class="coupon__pct">%</span><span>OFF</span></span></div>
    <div class="coupon__rule"></div>
    <div class="coupon__label">Synthetic Hair Extensions</div>
  </article>

  <article class="coupon" style="left:465px; top:712px;">
    <svg viewBox="0 0 290 173" width="290" height="173">
      <path d="M16,0 H274 A16,16 0 0 0 290,16 V157 A16,16 0 0 0 274,173 H16 A16,16 0 0 0 0,157 V16 A16,16 0 0 0 16,0 Z" fill="var(--white)"/>
      <path d="M22,6 H268 A16,16 0 0 0 284,22 V151 A16,16 0 0 0 268,167 H22 A16,16 0 0 0 6,151 V22 A16,16 0 0 0 22,6 Z" fill="none" stroke="var(--magenta)" stroke-width="1.2"/>
    </svg>
    <div class="coupon__figure"><span class="coupon__number">20</span><span class="coupon__unit"><span class="coupon__pct">%</span><span>OFF</span></span></div>
    <div class="coupon__rule"></div>
    <div class="coupon__label">Synthetic Hair Pieces</div>
  </article>

  <article class="coupon" style="left:123px; top:925px;">
    <svg viewBox="0 0 290 173" width="290" height="173">
      <path d="M16,0 H274 A16,16 0 0 0 290,16 V157 A16,16 0 0 0 274,173 H16 A16,16 0 0 0 0,157 V16 A16,16 0 0 0 16,0 Z" fill="var(--white)"/>
      <path d="M22,6 H268 A16,16 0 0 0 284,22 V151 A16,16 0 0 0 268,167 H22 A16,16 0 0 0 6,151 V22 A16,16 0 0 0 22,6 Z" fill="none" stroke="var(--magenta)" stroke-width="1.2"/>
    </svg>
    <div class="coupon__figure"><span class="coupon__number">15</span><span class="coupon__unit"><span class="coupon__pct">%</span><span>OFF</span></span></div>
    <div class="coupon__rule"></div>
    <div class="coupon__label">Human Hair Extensions</div>
  </article>

  <article class="coupon" style="left:465px; top:925px;">
    <svg viewBox="0 0 290 173" width="290" height="173">
      <path d="M16,0 H274 A16,16 0 0 0 290,16 V157 A16,16 0 0 0 274,173 H16 A16,16 0 0 0 0,157 V16 A16,16 0 0 0 16,0 Z" fill="var(--white)"/>
      <path d="M22,6 H268 A16,16 0 0 0 284,22 V151 A16,16 0 0 0 268,167 H22 A16,16 0 0 0 6,151 V22 A16,16 0 0 0 22,6 Z" fill="none" stroke="var(--magenta)" stroke-width="1.2"/>
    </svg>
    <div class="coupon__figure"><span class="coupon__number">25</span><span class="coupon__unit"><span class="coupon__pct">%</span><span>OFF</span></span></div>
    <div class="coupon__rule"></div>
    <div class="coupon__label">Jewelry/Accessories</div>
  </article>
</main>
</body>
</html>
```